Bref créative
Flyer, brochure, postcard
The Brennwick School
Where Curiosity Grows
This is a new high quality academic preschool from ages 6 weeks to pre-kindergarten. Early Childhood Campus. Logo and website were designed by Mark Forge; need to "brand" reputation for excellent early childhood education; by law all advertising must indicate it's opening August, 2012 or coming soon August 2012 somewhere on the flyer or postcard not on brochure;
Education
parents; families; caregivers with children under age 6; earning minimum of $75,000 per year; educated; both professionals and blue collar employees;
I would describe TBS by: exclusive, private, high quality, nurturing, loving, fun, building self-confidence in children, infants through pre-kindergarten; see website for more information and logo is provided; looking to "brand" a top notch reputation in early childhood education; we are different and want to stand out from other preschools; www.brennwickschool-example.com;
Content for Brochure
Content for Flyer

```html
<!DOCTYPE html>
<html lang="en">
<head>
<meta charset="utf-8">
<title>The Brennwick School – Tri-fold Brochure</title>
<link rel="stylesheet" href="https://fonts.googleapis.com/css2?family=Cinzel:wght@600&family=Open+Sans:wght@400;600;700&display=swap">
<style>
  :root {
    --navy-deep: #172a55;
    --navy: #25427c;
    --navy-light: #3a5d9e;
    --gold: #c9a24a;
    --gold-light: #e3c77c;
    --paper: #ffffff;
    --text-light: #e6ecf7;
    --backdrop: #e8e5e0;
  }
  * { box-sizing: border-box; margin: 0; padding: 0; }
  html, body { width: 1200px; height: 926px; overflow: hidden; }
  body { background: var(--backdrop); font-family: "Open Sans", sans-serif; position: relative; }

  .spread { position: absolute; top: 243px; width: 570px; height: 440px; display: flex; box-shadow: 0 4px 14px rgba(0,0,0,.25); }
  .spread--outside { left: 20px; }
  .spread--inside { left: 610px; }

  .panel { position: relative; width: 190px; height: 100%; overflow: hidden;
    background: linear-gradient(180deg, var(--navy-light) 0%, var(--navy) 45%, var(--navy-deep) 100%);
    color: var(--text-light); }
  .panel + .panel { border-left: 1px solid rgba(255,255,255,.12); }
  .panel--inside { background: linear-gradient(180deg, var(--navy) 0%, var(--navy-deep) 100%); }

  .gold-tab { display: inline-block; background: linear-gradient(90deg, var(--gold), var(--gold-light)); color: var(--navy-deep);
    font-weight: 700; font-size: 8px; letter-spacing: .5px; padding: 2px 10px 2px 8px; text-transform: uppercase; }
  .body-copy { font-size: 6.2px; line-height: 1.55; margin-bottom: 6px; }
  .panel-pad { padding: 10px 10px; }

  .photo { position: absolute; border: 2px solid var(--paper); }
  .photo--kids-pair { left: 0; bottom: 0; width: 190px; height: 110px; border: none;
    background: radial-gradient(circle at 40% 45%, #e8c9a6, #8a9fc4 70%, #3d5a8e); }
  .photo--classroom { left: 0; top: 70px; width: 190px; height: 180px; border: none;
    background: linear-gradient(135deg, #f2d36b 0%, #e07a4f 35%, #7ab0d9 70%, #3b6fb0 100%); }
  .photo--faded { left: 0; top: 250px; width: 190px; height: 190px; border: none; opacity: .55;
    background: linear-gradient(180deg, #d9a9a0 0%, #8aa8cf 60%, var(--navy) 100%); }
  .photo--map { left: 48px; top: 320px; width: 95px; height: 55px; background: linear-gradient(135deg, #f1f0e8, #cfd8c6); }

  .name-mark { display: flex; align-items: center; justify-content: center; gap: 6px; }
  .name-mark__dot { width: 10px; height: 10px; border-radius: 50%; background: var(--gold); }
  .name-mark__text { font-family: "Cinzel", serif; font-weight: 600; color: var(--gold-light); }

  .mail-logo { position: absolute; top: 60px; left: 0; width: 190px; text-align: center; }
  .mail-logo .name-mark__text { font-size: 15px; line-height: 1.2; }
  .mail-band { position: absolute; top: 220px; left: 0; width: 190px; height: 22px;
    background: linear-gradient(90deg, var(--gold), var(--gold-light), var(--gold));
    color: var(--navy-deep); font-weight: 700; font-size: 10px; text-transform: uppercase; letter-spacing: 1px;
    display: flex; align-items: center; justify-content: center; }
  .mail-address { position: absolute; top: 258px; width: 190px; text-align: center; font-size: 7px; line-height: 1.6; }

  .cover-band { position: absolute; top: 14px; left: 0; width: 190px; height: 44px;
    background: linear-gradient(90deg, var(--gold), var(--gold-light)); display: flex; align-items: center; justify-content: center; }
  .cover-band .name-mark__text { color: var(--navy-deep); font-size: 13px; }
  .cover-band .name-mark__dot { background: var(--navy-deep); }

  .inside-title { font-family: "Cinzel", serif; font-weight: 600; color: var(--gold-light); font-size: 10px; margin-bottom: 6px; }
  .thumb-row { display: flex; gap: 5px; margin-bottom: 8px; }
  .thumb { height: 58px; flex: 1; border: 2px solid var(--paper); }
  .thumb--warm { background: linear-gradient(135deg, #f3d7b5, #c98d6d); }
  .thumb--cool { background: linear-gradient(135deg, #bcd3ec, #6c8fc4); }
  .thumb--bright { background: linear-gradient(135deg, #f6e08a, #e58b5a); }
  .thumb--tall { height: 90px; }
</style>
</head>
<body>

<section class="spread spread--outside" aria-label="Brochure outside">
  <article class="panel panel-about">
    <div class="panel-pad">
      <span class="gold-tab">About</span>
      <p class="body-copy" style="margin-top:8px">The Brennwick School is a new academic preschool for children from six weeks to pre-kindergarten. Our early childhood campus offers a warm, safe and joyful place where young minds grow with care every day.</p>
      <p class="body-copy">Small classes, caring teachers and a rich daily program help each child build confidence, kindness and a lifelong love of learning.</p>
      <p class="body-copy">Visit our campus to meet our staff, tour the classrooms and see how we nurture every family.</p>
    </div>
    <div class="photo photo--kids-pair" role="img" aria-label="Photo of two smiling young children"></div>
  </article>

  <article class="panel panel-mailing">
    <div class="mail-logo">
      <div class="name-mark"><span class="name-mark__dot"></span><span class="name-mark__text">The Brennwick<br>School</span></div>
    </div>
    <div class="mail-band">Mailing Address</div>
    <div class="mail-address">
      4120 Larkspur Lane<br>Westfield Bay, FL 33000<br>555-0142<br>www.brennwickschool-example.com
    </div>
    <div class="photo photo--map" role="img" aria-label="Location map of the campus"></div>
  </article>

  <article class="panel panel-cover">
    <div class="cover-band">
      <div class="name-mark"><span class="name-mark__dot"></span><span class="name-mark__text">The Brennwick School</span></div>
    </div>
    <div class="photo photo--classroom" role="img" aria-label="Photo of preschoolers playing together at a classroom table"></div>
    <div class="photo photo--faded" role="img" aria-label="Soft faded photo of a child at play"></div>
  </article>
</section>

<section class="spread spread--inside" aria-label="Brochure inside">
  <article class="panel panel--inside panel-pad">
    <div class="thumb-row">
      <div class="thumb thumb--warm" role="img" aria-label="Photo of a toddler"></div>
      <div class="thumb thumb--cool" role="img" aria-label="Photo of a teacher with an infant"></div>
    </div>
    <h2 class="inside-title">Mission &amp; What we Believe</h2>
    <p class="body-copy">The mission of The Brennwick School is to provide a loving, stimulating setting where every child feels valued, safe and eager to explore the world around them.</p>
    <p class="body-copy">We believe in play-based learning, strong partnerships with parents and teachers who treat each child as a unique person with gifts to share.</p>
    <div class="thumb-row">
      <div class="thumb thumb--bright" role="img" aria-label="Photo of children building with blocks"></div>
      <div class="thumb thumb--warm" role="img" aria-label="Photo of a child painting"></div>
    </div>
  </article>

  <article class="panel panel--inside panel-pad">
    <span class="gold-tab">Our Programs</span>
    <p class="body-copy" style="margin-top:8px">Infant, toddler and preschool rooms are designed for each stage of growth, with gentle routines, music, art, language and early math woven into every day.</p>
    <div class="thumb-row">
      <div class="thumb thumb--cool thumb--tall" role="img" aria-label="Photo of a reading circle"></div>
    </div>
    <p class="body-copy">Our pre-kindergarten class prepares children for school with reading readiness, science projects and outdoor discovery.</p>
    <div class="thumb-row">
      <div class="thumb thumb--bright" role="img" aria-label="Photo of a child smiling in class"></div>
      <div class="thumb thumb--cool" role="img" aria-label="Photo of toddlers at play"></div>
    </div>
  </article>

  <article class="panel panel--inside panel-pad">
    <span class="gold-tab">Our Campus</span>
    <p class="body-copy" style="margin-top:8px">Bright classrooms, secure entry, a shaded playground and a family lounge make our campus a second home for children and parents alike.</p>
    <div class="thumb-row">
      <div class="thumb thumb--warm thumb--tall" role="img" aria-label="Photo of the playground"></div>
    </div>
    <p class="body-copy">Call or visit today to schedule a personal tour and reserve a place for your child.</p>
    <div class="thumb-row">
      <div class="thumb thumb--cool thumb--tall" role="img" aria-label="Photo of a child on a slide"></div>
    </div>
  </article>
</section>

</body>
</html>
```